Business Landing Page for SEO Company

Need the landing page of the website designed - I will provide the copy, will need to include details of my company and the services offered, about us, testimonials, faq, etc., and all these elements will need to be arranged graphically on the page.

I want something similar to this: https://pebrovault.com/

Not in terms of color or theme or anything, but we offer a similar service and want to display similar information.

Th services we provide are:

Premium Links
Monthly Links Subscription
Link Insertions

Need to advertise them on the front page. Additionally need a place for testimonials, company details, etc.,

We already have logo for the website. Please use the attached file to insert the logo within the overal design.

Target Market(s)

SEO marketers and agencies

Number of Pages Required

1 page

```html
<!DOCTYPE html>
<html lang="en">
<head>
<meta charset="utf-8">
<title>Linkora – SEO Link Building</title>
<link rel="stylesheet" href="https://fonts.googleapis.com/css2?family=Kanit:wght@300;400;500;600&family=Montserrat:wght@400;500;600;700&display=swap">
<style>
:root{
  --blue:#2f88e3;
  --blue-dark:#1f6fc9;
  --navy:#1c2b4a;
  --orange:#f7901e;
  --orange-deep:#f57a0c;
  --ink:#333a45;
  --muted:#6b7280;
  --gray-bg:#f1f2f4;
  --footer:#242424;
  --white:#fff;
}
*{box-sizing:border-box;margin:0;padding:0}
html,body{width:1200px;height:5102px;overflow:hidden;background:var(--white)}
body{font-family:"Montserrat",sans-serif;color:var(--ink)}
.page{position:relative;width:1200px;height:5102px;overflow:hidden}
.abs{position:absolute}

/* header */
.logo{left:58px;top:20px;font:500 50px/1 "Kanit",sans-serif;color:var(--blue);display:flex;align-items:center;gap:6px}
.logo .dot{width:12px;height:12px;background:var(--orange);border-radius:50%}
.callus{left:770px;top:26px;font-size:15px;color:var(--navy);display:flex;gap:8px;align-items:center}
.livechat{left:1010px;top:20px;width:120px;height:34px;border-radius:17px;background:var(--blue);color:#fff;font-size:11px;font-weight:600;display:flex;align-items:center;justify-content:center;gap:6px}
.nav{left:525px;top:76px;display:flex;gap:34px;font-size:16px;font-weight:500;color:var(--navy);letter-spacing:.2px}

/* hero */
.hero-photo{left:0;top:0;width:1200px;height:700px;background:linear-gradient(100deg,#fbfaf8 0%,#f1ece6 45%,#c9bfb4 70%,#8d7c6d 100%)}
.hero-title{left:123px;top:205px;font:500 37px/48px "Kanit",sans-serif;color:var(--navy);text-transform:uppercase}
.hero-title b{color:var(--blue);font-weight:500}
.ticks{left:123px;top:330px;list-style:none;font-size:17px;color:var(--navy);line-height:37px}
.ticks li{display:flex;align-items:center;gap:14px}
.btn{display:flex;align-items:center;justify-content:center;border-radius:26px;font-size:17px}
.btn-orange{background:var(--orange);color:#fff}
.btn-blue{background:var(--blue);color:#fff}
.btn-outline{border:2px solid var(--blue);color:var(--blue);background:#fff;font-weight:600}
.slider-dots{left:1080px;top:308px;display:flex;flex-direction:column;gap:12px}
.slider-dots i{width:13px;height:13px;border-radius:50%;background:#b8bcc4;display:block}
.slider-dots i.on{background:var(--blue)}
.stats{left:0;top:740px;width:1200px;display:flex}
.stat{width:300px;height:150px;display:flex;flex-direction:column;align-items:center;justify-content:center;gap:18px;color:#fff;font-weight:600;font-size:15px;position:relative}
.stat+.stat::before{content:"";position:absolute;left:0;top:22px;height:110px;border-left:1px solid rgba(255,255,255,.45)}

/* headings */
.sec-title{width:1200px;left:0;text-align:center;font:300 44px/1 "Kanit",sans-serif;color:var(--navy)}
.sec-title b{font-weight:500}

/* services */
.svc{width:312px;height:252px;background:#fff;border:1px solid #dde0e5;box-shadow:0 2px 6px rgba(0,0,0,.12);top:1162px;text-align:center;padding-top:76px}
.svc .ico{position:absolute;left:110px;top:-46px;width:92px;height:92px;border-radius:50%;background:#3a3a3a;display:flex;align-items:center;justify-content:center}
.svc.active .ico{background:var(--blue)}
.svc h3{font-size:15px;font-weight:600;color:var(--navy)}
.svc p{font-size:12.5px;line-height:19px;color:var(--muted);margin:12px auto 0;width:240px}
.svc .btn{width:150px;height:40px;margin:16px auto 0;font-size:13px}

/* who we are */
.who{left:0;top:1540px;width:1200px;height:682px;background:linear-gradient(180deg,#3a8ee2,#2a7fd8 60%,#2d83dc)}
.who-title{top:1600px;color:#fff}
.who-sub{top:1660px;left:0;width:1200px;text-align:center;color:#fff;font-size:16px}
.who-photo{left:346px;top:1723px;width:484px;height:548px;background:linear-gradient(160deg,#e7e8ea,#9aa3ad 55%,#3e4650)}
.tag{width:290px;height:138px}
.tag .band{position:absolute;inset:0 0 0 40px;background:var(--blue);clip-path:polygon(18% 0,100% 0,82% 100%,0 100%)}
.tag .disc{position:absolute;left:0;top:0;width:138px;height:138px;border-radius:50%;background:#fff;display:flex;align-items:center;justify-content:center}
.tag .txt{position:absolute;left:150px;top:0;height:138px;display:flex;flex-direction:column;justify-content:center;color:#fff;font-size:15px;line-height:19px}
.tag .txt strong{font:500 26px/1.1 "Kanit",sans-serif}

/* why */
.why-bg{left:0;top:2376px;width:1200px;height:578px}
.why-title{left:115px;top:2518px;font:500 40px/1 "Kanit",sans-serif;color:var(--navy)}
.why-text{left:115px;top:2586px;width:450px;font-size:15px;line-height:24px;color:#444}
.why-photo{left:614px;top:2489px;width:437px;height:344px;background:linear-gradient(120deg,#5b636c,#c9cdd2 50%,#8f9aa6);z-index:2}
.why-frame{left:643px;top:2528px;width:436px;height:331px;border:5px solid var(--blue);border-radius:3px}
.why-blob{left:1125px;top:2505px;width:380px;height:376px;border-radius:50%;background:var(--blue)}

/* cta */
.cta-bg{left:0;top:2990px;width:1200px;height:645px}
.cta-art{left:124px;top:3223px;width:318px;height:318px;border-radius:50%;background:radial-gradient(circle,var(--blue) 0 60%,rgba(255,255,255,.12) 61% 100%)}
.cta-small{left:556px;top:3250px;font:300 32px/1 "Kanit",sans-serif;color:#fff}
.cta-big{left:556px;top:3300px;font:500 42px/52px "Kanit",sans-serif;color:#fff}
.cta-photo{left:940px;top:3128px;width:220px;height:555px;background:linear-gradient(180deg,rgba(255,255,255,.10),rgba(255,255,255,.03))}

/* reviews */
.review{top:3811px;width:292px;height:307px;background:#fff;border-radius:18px;box-shadow:0 6px 22px rgba(0,0,0,.1);padding:36px 30px 36px 38px}
.review h4{font-size:18px;line-height:26px;font-weight:600;color:var(--navy)}
.review p{font-size:13px;line-height:22px;color:var(--muted);margin-top:20px}
.review .who-line{display:flex;align-items:center;gap:14px;margin-top:18px}
.review .av{width:44px;height:44px;border-radius:50%;background:linear-gradient(#cbd3dc,#8c97a3)}
.review .stars{color:var(--orange);font-size:13px;letter-spacing:1px}
.review .name{font-size:12px;font-weight:600;color:var(--navy)}

/* form */
.field{height:42px;border:1px solid #b7bcc3;font-size:15px;color:#555;padding:0 18px;display:flex;align-items:center;background:#fff}

/* footer */
.footer{left:0;top:4780px;width:1200px;height:322px;background:var(--footer)}
.cbox{width:228px;height:121px;background:var(--blue);color:#fff;text-align:center;padding-top:34px}
.cbox h5{font:500 22px/1 "Kanit",sans-serif}
.cbox p{font-size:13px;margin-top:14px;line-height:18px}
.cbox .ci{position:absolute;left:-4px;top:-26px}
.fcol{top:4898px;color:#fff;font-size:15px;line-height:25px}
.fcol.links{font-size:12px;line-height:30px}
.fcol.links span{display:block;text-decoration:underline}
.fcol.links .head{text-decoration:none;font-size:15px;line-height:22px}
.map{left:786px;top:4883px;width:281px;height:126px;background:linear-gradient(135deg,#e9edf2,#d6dde6 60%,#c8d3df)}
.social{left:524px;top:5054px;display:flex;gap:8px}
.social i{width:32px;height:32px;border-radius:50%;border:1.5px solid #cfcfcf;display:block}
</style>
</head>
<body>
<div class="page">

  <!-- hero -->
  <div class="abs hero-photo" role="img" aria-label="Smiling man with a coffee mug working at a laptop in a bright office"></div>
  <svg class="abs" style="left:0;top:0" width="1200" height="956" viewBox="0 0 1200 956">
    <path d="M0,566 C220,600 420,705 640,700 C860,695 1030,630 1200,560 L1200,956 L0,956Z" fill="var(--blue)"/>
  </svg>

  <div class="abs logo"><span>linkora</span><span class="dot"></span></div>
  <div class="abs callus">
    <svg width="18" height="18" viewBox="0 0 24 24" fill="none" stroke="#1c2b4a" stroke-width="1.8"><path d="M5 3h4l2 5-3 2a12 12 0 006 6l2-3 5 2v4a2 2 0 01-2 2A18 18 0 013 5a2 2 0 012-2z"/></svg>
    <span>Call us : 888-555010</span>
  </div>
  <div class="abs livechat">
    <svg width="14" height="14" viewBox="0 0 24 24" fill="#fff"><path d="M4 4h16v11H9l-5 4z"/></svg>LIVE CHAT
  </div>
  <nav class="abs nav"><span>HOME</span><span>ABOUT US</span><span>SERVICES</span><span>TESTIMONIALS</span><span>FAQ</span><span>BLOG</span></nav>

  <h1 class="abs hero-title"><b>Boost</b> your position in<br>search engines with <b>Linkora</b></h1>
  <ul class="abs ticks">
    <li><svg width="18" height="18" viewBox="0 0 20 20" fill="none" stroke="var(--blue)" stroke-width="1.6"><circle cx="10" cy="10" r="8"/><path d="M6 10l3 3 5-6"/></svg>Trusted by People Like You</li>
    <li><svg width="18" height="18" viewBox="0 0 20 20" fill="none" stroke="var(--blue)" stroke-width="1.6"><circle cx="10" cy="10" r="8"/><path d="M6 10l3 3 5-6"/></svg>Complete Technical Competency</li>
    <li><svg width="18" height="18" viewBox="0 0 20 20" fill="none" stroke="var(--blue)" stroke-width="1.6"><circle cx="10" cy="10" r="8"/><path d="M6 10l3 3 5-6"/></svg>Excellent Quality Delivered on Time</li>
  </ul>
  <div class="abs btn btn-orange" style="left:123px;top:471px;width:196px;height:50px;gap:14px">Get Started
    <svg width="26" height="12" viewBox="0 0 26 12" fill="none" stroke="#fff" stroke-width="1.6"><path d="M0 6h24M19 1l5 5-5 5"/></svg></div>
  <div class="abs slider-dots"><i></i><i class="on"></i><i></i></div>

  <div class="abs stats">
    <div class="stat"><svg width="64" height="64" viewBox="0 0 64 64" fill="none" stroke="#fff" stroke-width="2"><path d="M32 56S8 40 8 22a12 12 0 0124-4 12 12 0 0124 4c0 18-24 34-24 34z"/><circle cx="32" cy="26" r="6"/><path d="M22 44c2-7 18-7 20 0"/></svg>450 HAPPY CLIENTS</div>
    <div class="stat"><svg width="64" height="64" viewBox="0 0 64 64" fill="none" stroke="#fff" stroke-width="2"><path d="M32 22S20 14 20 8a6 6 0 0112-1 6 6 0 0112 1c0 6-12 14-12 14z"/><circle cx="14" cy="40" r="5"/><circle cx="32" cy="40" r="5"/><circle cx="50" cy="40" r="5"/><path d="M5 58c2-8 16-8 18 0M23 58c2-8 16-8 18 0M41 58c2-8 16-8 18 0M32 22v12"/></svg>48K PROJECTS DONE</div>
    <div class="stat"><svg width="64" height="64" viewBox="0 0 64 64" fill="none" stroke="#fff" stroke-width="2"><circle cx="32" cy="20" r="12"/><path d="M26 20l4 4 8-8"/><circle cx="14" cy="42" r="5"/><circle cx="50" cy="42" r="5"/><circle cx="32" cy="44" r="5"/><path d="M5 60c2-8 16-8 18 0M41 60c2-8 16-8 18 0M23 62c2-8 16-8 18 0"/></svg>QUALITY DELIVERED</div>
    <div class="stat"><svg width="64" height="64" viewBox="0 0 64 64" fill="none" stroke="#fff" stroke-width="2"><circle cx="28" cy="34" r="9"/><path d="M14 58c3-10 25-10 28 0M17 34a11 11 0 0122 0"/><rect x="38" y="6" width="20" height="14" rx="2"/><path d="M8 22a24 24 0 0118-14"/></svg>24/7 SUPPORT</div>
  </div>

  <!-- services -->
  <h2 class="abs sec-title" style="top:1033px">Services <b>We Offerd</b></h2>
  <div class="abs svc" style="left:107px">
    <div class="ico"><svg width="52" height="52" viewBox="0 0 52 52" fill="none" stroke="#fff" stroke-width="2"><circle cx="28" cy="17" r="11"/><path d="M28 10v14M31 13h-5a2.5 2.5 0 000 5h4a2.5 2.5 0 010 5h-5"/><path d="M4 36h8l8 4h10a3 3 0 010 6H18M12 46l10 4h18l10-10"/></svg></div>
    <h3>PREMIUM LINKS</h3>
    <p>Lorem Ipsum is simply dummy text of the printing and typesetting industry. Lorem Ipsum has been</p>
    <div class="btn btn-outline">LEARN MORE</div>
  </div>
  <div class="abs svc active" style="left:444px">
    <div class="ico"><svg width="52" height="52" viewBox="0 0 52 52" fill="none" stroke="#fff" stroke-width="2"><circle cx="28" cy="17" r="11"/><path d="M28 10v14M31 13h-5a2.5 2.5 0 000 5h4a2.5 2.5 0 010 5h-5"/><path d="M4 36h8l8 4h10a3 3 0 010 6H18M12 46l10 4h18l10-10"/></svg></div>
    <h3>MONTHLY LINKS SUBSCRIPTION</h3>
    <p>Lorem Ipsum is simply dummy text of the printing and typesetting industry. Lorem Ipsum has been</p>
    <div class="btn btn-outline">LEARN MORE</div>
  </div>
  <div class="abs svc" style="left:781px">
    <div class="ico"><svg width="52" height="52" viewBox="0 0 52 52" fill="none" stroke="#fff" stroke-width="2"><circle cx="28" cy="17" r="11"/><path d="M28 10v14M31 13h-5a2.5 2.5 0 000 5h4a2.5 2.5 0 010 5h-5"/><path d="M4 36h8l8 4h10a3 3 0 010 6H18M12 46l10 4h18l10-10"/></svg></div>
    <h3>LINK INSERTIONS</h3>
    <p>Lorem Ipsum is simply dummy text of the printing and typesetting industry. Lorem Ipsum has been</p>
    <div class="btn btn-outline">LEARN MORE</div>
  </div>

  <!-- who we are -->
  <div class="abs who" role="img" aria-label="Blue-tinted photo of a team working in an office"></div>
  <h2 class="abs sec-title who-title"><b>Who</b> We Are</h2>
  <p class="abs who-sub">The Benefits of Working in Social Media Management</p>
  <div class="abs who-photo" role="img" aria-label="Team meeting with a presenter at a whiteboard and colleagues at laptops"></div>

  <div class="abs tag" style="left:103px;top:1855px"><div class="band"></div>
    <div class="disc"><svg width="54" height="54" viewBox="0 0 54 54" fill="none" stroke="var(--blue)" stroke-width="2"><path d="M6 48h42M12 48V34M22 48V28M32 48V22M42 48V14M10 28l12-10 10 6 14-14M40 10h6v6"/></svg></div>
    <div class="txt"><strong>15 +</strong>Years of<br>Experience</div></div>
  <div class="abs tag" style="left:100px;top:2013px"><div class="band"></div>
    <div class="disc"><svg width="54" height="54" viewBox="0 0 54 54" fill="none" stroke="var(--blue)" stroke-width="2"><circle cx="27" cy="12" r="6"/><path d="M17 30c2-8 18-8 20 0M8 38l10 10h18l10-10M14 34l13 8 13-8"/></svg></div>
    <div class="txt">Dedicated<br>Team of<br>Experts</div></div>
  <div class="abs tag" style="left:772px;top:1855px"><div class="band"></div>
    <div class="disc"><svg width="54" height="54" viewBox="0 0 54 54" fill="none" stroke="var(--blue)" stroke-width="2"><circle cx="27" cy="26" r="10"/><path d="M13 26a14 14 0 0128 0M11 24h4v8h-4zM39 24h4v8h-4zM18 46c3-6 15-6 18 0"/></svg></div>
    <div class="txt">Full Online<br>Support</div></div>
  <div class="abs tag" style="left:772px;top:2013px"><div class="band"></div>
    <div class="disc"><svg width="54" height="54" viewBox="0 0 54 54" fill="none" stroke="var(--blue)" stroke-width="2"><circle cx="27" cy="27" r="8"/><circle cx="10" cy="14" r="5"/><circle cx="44" cy="14" r="5"/><circle cx="10" cy="40" r="5"/><circle cx="44" cy="40" r="5"/><path d="M14 17l7 5M40 17l-7 5M14 37l7-5M40 37l-7-5"/></svg></div>
    <div class="txt">Free<br>Mainantance<br>&amp; Support</div></div>

  <!-- why choose us -->
  <svg class="abs why-bg" width="1200" height="578" viewBox="0 0 1200 578">
    <path d="M0,0 H640 C760,0 800,120 960,126 H1200 V578 H0Z" fill="var(--gray-bg)"/>
  </svg>
  <div class="abs why-blob"></div>
  <h2 class="abs why-title">Why Choose Us</h2>
  <p class="abs why-text">Lorem Ipsum is simply dummy text of the printing and typesetting industry. Lorem Ipsum has been industry's standard dummy text ever since the 1500s, when an unknown printer took a galley of type and scrambled.</p>
  <div class="abs btn btn-outline" style="left:115px;top:2726px;width:168px;height:48px;font-size:15px;font-weight:500">LEARN MORE</div>
  <div class="abs why-frame"></div>
  <div class="abs why-photo" role="img" aria-label="Couple receiving car keys from a sales agent in a showroom"></div>

  <!-- call to action -->
  <svg class="abs cta-bg" width="1200" height="645" viewBox="0 0 1200 645">
    <defs><linearGradient id="og" x1="0" y1="0" x2="1" y2="1"><stop offset="0" stop-color="#fb9a22"/><stop offset="1" stop-color="#f57a0c"/></linearGradient></defs>
    <path d="M0,10 C260,60 480,110 720,100 C920,90 1060,70 1200,80 V645 H0Z" fill="url(#og)"/>
  </svg>
  <div class="abs cta-art" role="img" aria-label="Illustration of a white paper plane on a blue circle"></div>
  <p class="abs cta-small">Change starts here</p>
  <p class="abs cta-big">Take your first step<br>towards RESULT.</p>
  <div class="abs btn btn-blue" style="left:560px;top:3451px;width:194px;height:48px;font-size:16px">Email us Today</div>
  <div class="abs cta-photo" role="img" aria-label="Photo of a woman in a red top and jeans holding a phone"></div>

  <!-- reviews -->
  <h2 class="abs sec-title" style="top:3720px">Client <b>Reviews</b></h2>
  <svg class="abs" style="left:70px;top:3938px" width="34" height="20" viewBox="0 0 34 20" fill="none" stroke="#6b7280" stroke-width="2"><path d="M34 10H2M10 2L2 10l8 8"/></svg>
  <svg class="abs" style="left:1094px;top:3938px" width="34" height="20" viewBox="0 0 34 20" fill="none" stroke="var(--blue)" stroke-width="2"><path d="M0 10h32M24 2l8 8-8 8"/></svg>
  <div class="abs review" style="left:133px">
    <h4>Lorem Ipsum is simply<br>dummy text of the</h4>
    <p>Lorem Ipsum is simply dummy text of the printing and typesetting industry. Lorem Ipsum has been the industry's</p>
    <div class="who-line"><div class="av" role="img" aria-label="Reviewer portrait"></div><div><div class="stars">★★★★★</div><div class="name">DANA HOLT</div></div></div>
  </div>
  <div class="abs review" style="left:454px">
    <h4>Lorem Ipsum is simply<br>dummy text of the</h4>
    <p>Lorem Ipsum is simply dummy text of the printing and typesetting industry. Lorem Ipsum has been the industry's</p>
    <div class="who-line"><div class="av" role="img" aria-label="Reviewer portrait"></div><div><div class="stars">★★★★★</div><div class="name">DANA HOLT</div></div></div>
  </div>
  <div class="abs review" style="left:775px">
    <h4>Lorem Ipsum is simply<br>dummy text of the</h4>
    <p>Lorem Ipsum is simply dummy text of the printing and typesetting industry. Lorem Ipsum has been the industry's</p>
    <div class="who-line"><div class="av" role="img" aria-label="Reviewer portrait"></div><div><div class="stars">★★★★★</div><div class="name">DANA HOLT</div></div></div>
  </div>
  <div class="abs btn btn-orange" style="left:503px;top:4172px;width:194px;height:48px;font-size:15px">View all Reviews</div>

  <!-- contact form -->
  <h2 class="abs sec-title" style="top:4292px">Get In <b>Touch</b></h2>
  <div class="abs field" style="left:273px;top:4376px;width:313px">Your Name</div>
  <div class="abs field" style="left:612px;top:4376px;width:313px">Subject</div>
  <div class="abs field" style="left:273px;top:4447px;width:313px">Email Address</div>
  <div class="abs field" style="left:273px;top:4518px;width:313px">Phone</div>
  <div class="abs field" style="left:612px;top:4447px;width:313px;height:115px"></div>
  <div class="abs btn btn-outline" style="left:517px;top:4600px;width:166px;height:46px;font-size:16px;font-weight:500;color:var(--navy)">Email us</div>

  <!-- footer -->
  <div class="abs footer"></div>
  <div class="abs cbox" style="left:232px;top:4726px">
    <svg class="ci" width="44" height="34" viewBox="0 0 44 34" fill="var(--blue)" stroke="#fff" stroke-width="2"><rect x="2" y="2" width="40" height="30"/><path d="M2 2l20 16L42 2" fill="none"/></svg>
    <h5>Write Us</h5><p>contact@company.com</p></div>
  <div class="abs cbox" style="left:485px;top:4706px;height:121px;padding-top:30px">
    <svg class="ci" style="left:4px;top:-22px" width="30" height="42" viewBox="0 0 30 42" fill="var(--blue)" stroke="#fff" stroke-width="2"><path d="M15 40S2 24 2 15a13 13 0 0126 0c0 9-13 25-13 25z"/><circle cx="15" cy="15" r="5" fill="#fff"/></svg>
    <h5>Visit Us</h5><p>Lorem Ipsum is<br>simply dummy text of</p></div>
  <div class="abs cbox" style="left:739px;top:4726px">
    <svg class="ci" style="top:-30px" width="42" height="42" viewBox="0 0 24 24" fill="var(--blue)" stroke="#fff" stroke-width="1.5"><path d="M5 3h4l2 5-3 2a12 12 0 006 6l2-3 5 2v4a2 2 0 01-2 2A18 18 0 013 5a2 2 0 012-2z"/></svg>
    <h5>Call Us</h5><p>(000) 888 8888</p></div>

  <div class="abs fcol" style="left:131px">Home<br>About Us<br>Services<br>Testimonials<br>FAQ</div>
  <div class="abs fcol links" style="left:327px"><span class="head">Services</span><span>Premium Links</span><span>Monthly Links Subscription</span><span>Link Insertions</span></div>
  <div class="abs fcol links" style="left:576px"><span class="head">Quick Contact</span><span>FAQ</span><span>Testimonials</span><span>Contact Us</span></div>
  <div class="abs map" role="img" aria-label="Street map showing the office location"></div>
  <div class="abs social"><i></i><i></i><i></i><i></i></div>

</div>
</body>
</html>
```